WP website design for Colbury

We need a wordpress design for an established auction and real estate company based in New Jersey. The winning design will incorporate a professional color scheme with company logo in a clean layout. The design needs to consider that this will be developed on a responsive theme. Colors are those that will highlight the logo

Industry/Entity Type

Real Estate

Font styles to use
Serif
Sans Serif

Requirements
Must have
• colors will be #3E3D5D and #3C7296
navigation: 1) Home 2) Auctions 3) Real Estate Listings 4) Buyers 5) Sellers 6) About Us 7 ) Contact Us
design will use a slideshow - image is attached.
Widgets to place in the header, sidebar or footer:
1) email signup form 2) social icons (facebook, twitter, youtube, RSS) 3) Featured Properties widget 4) Featured Auctions widget 5) News & Events blog 6) Featured Videos
Nice to have
• Site will have numerous dropdown menus - so it would be nice to have a sample of what the dropdowns would look like. EG 1)▪ Our Featured Listings and 2)▪ MLS Property Search under the main "Real Estate Listings" menu item.

```html
<!DOCTYPE html>
<html lang="en">
<head>
<meta charset="utf-8">
<title>Colbury Real Estate &amp; Auction</title>
<link rel="stylesheet" href="https://fonts.googleapis.com/css2?family=Open+Sans:wght@400;600;700&display=swap">
<style>
:root{
  --navy:#3E3D5D;
  --blue:#3C7296;
  --blue-light:#4a80a6;
  --ink:#3b3b4a;
  --muted:#9a9aa6;
  --line:#e6e6ea;
  --gold:#f0a22a;
  --footer:#1d2131;
  --footer-text:#7d8293;
  --white:#ffffff;
}
*{margin:0;padding:0;box-sizing:border-box}
html,body{width:1200px;height:2179px;overflow:hidden;background:var(--white)}
body{position:relative;font-family:"Open Sans",Arial,sans-serif;color:var(--ink)}
.abs{position:absolute}

/* header */
.brand{left:171px;top:40px;display:flex;align-items:center;gap:10px}
.brand-square{width:34px;height:34px;background:var(--blue)}
.brand-name{font-size:30px;font-weight:700;color:var(--navy);letter-spacing:.5px}
.social-top{left:910px;top:24px;display:flex;gap:6px}
.social-top span{width:25px;height:25px;border-radius:50%;background:var(--blue)}
.social-top span:nth-child(even){background:var(--navy)}
.search{left:800px;top:77px;width:172px;height:38px;border:1px solid var(--line);font-size:11px;color:#b9b9c2;padding:11px 16px}
.search-btn{left:982px;top:77px;width:47px;height:38px;border:1px solid var(--line);display:flex;align-items:center;justify-content:center}

/* nav */
.nav{left:0;top:141px;width:1200px;height:48px;background:var(--blue);border-top:1px solid #2f5f80}
.nav a{position:absolute;top:0;height:47px;line-height:47px;color:var(--white);font-size:15.5px;text-decoration:none}
.nav .sep{position:absolute;top:0;width:1px;height:47px;background:rgba(255,255,255,.12)}
.dropdown{left:389px;top:193px;width:191px}
.dropdown a{display:block;height:43.5px;line-height:43.5px;padding-left:16px;color:var(--white);font-size:13px;text-decoration:none}
.dropdown a.first{background:var(--blue-light)}
.dropdown a.second{background:var(--navy)}

/* hero */
.hero{left:0;top:189px;width:1200px;height:439px;background:linear-gradient(180deg,#9db6cf 0%,#c9d6e1 32%,#6f8a70 50%,#4e8a2c 62%,#5ea332 100%)}
.hero-caption{left:398px;top:372px;width:429px;height:126px;background:rgba(30,34,40,.55);padding:6px 16px 0}
.hero-caption h1{font-size:45px;font-weight:400;color:var(--white);line-height:58px;margin-left:-2px}
.hero-caption p{font-size:11.5px;line-height:18px;color:#eef0f2;margin-top:8px}
.hero-arrow{top:408px;width:36px;height:36px;border-radius:50%;background:rgba(0,0,0,.75);display:flex;align-items:center;justify-content:center}

/* welcome */
.video{left:171px;top:655px;width:266px;height:202px;background:linear-gradient(180deg,#8fb3d6 0%,#c8d3d8 40%,#6d8c55 75%,#4f7a34 100%)}
.video-bar{left:171px;top:826px;width:266px;height:31px;background:#111;display:flex;align-items:center;padding:0 10px;gap:8px;color:#ddd;font-size:9px}
.video-track{flex:1;height:5px;background:#555;position:relative}
.video-track i{position:absolute;left:0;top:0;height:5px;width:55%;background:#eee}
.welcome-title{left:462px;top:648px;font-size:25px;font-weight:600;color:var(--navy)}
.welcome-text{left:462px;top:690px;width:567px;font-size:11.2px;line-height:21px;color:var(--muted);text-align:justify}
.badge{top:808px;height:42px;background:#2a2a33}
.badge.outline{background:none;border:2px solid #2a2a33}

/* sections */
.section-title{left:171px;font-size:20px;color:var(--navy)}
.pager{display:flex;gap:8px}
.pager span{width:18px;height:18px;border-radius:50%;border:1px solid #d5d5dc;display:flex;align-items:center;justify-content:center}
.card{width:203px;border:1px solid #eeeef1;background:var(--white)}
.card-img{display:block;width:100%}
.card-body{padding:14px 14px 0}
.card-title{font-size:15.5px;color:#6a6a76}
.card-meta{display:flex;align-items:center;gap:20px;margin-top:8px;font-size:10.5px;color:#8a8a96}
.stars{color:var(--gold);font-size:11px;letter-spacing:1px}
.stars b{color:#cfcfd6;font-weight:400}
.card-text{margin-top:12px;font-size:10.5px;line-height:20px;color:#a5a5b0;text-align:justify}

/* news */
.rule{left:171px;top:1665px;width:858px;height:1px;background:var(--line)}
.news-img{width:191px;height:166px}
.news-body{width:204px}
.news-title{font-size:15px;color:#55556a}
.news-date{font-size:11px;color:var(--gold);margin-top:10px}
.news-text{font-size:10.5px;line-height:20px;color:#9d9da8;margin-top:8px;text-align:justify}
.news-link{font-size:10.5px;color:var(--gold);margin-top:10px}

/* footer */
.footer{left:0;top:1894px;width:1200px;height:285px;background:var(--footer)}
.footer-brand{left:171px;top:1924px;display:flex;align-items:center;gap:10px}
.footer-brand .sq{width:30px;height:30px;background:#3a4053}
.footer-brand span{font-size:24px;font-weight:700;color:#3a4053}
.footer-about{left:171px;top:1978px;width:250px;font-size:11px;line-height:20.5px;color:var(--footer-text);text-align:justify}
.footer-head{top:1944px;font-size:14.5px;color:#8f94a4;letter-spacing:.5px}
.addr-row{left:492px;display:flex;gap:12px;font-size:11px;color:var(--footer-text);align-items:flex-start;line-height:20px}
.addr-row svg{flex:none;margin-top:3px}
.newsletter-text{left:747px;top:1978px;width:282px;font-size:11px;line-height:20.5px;color:var(--footer-text)}
.news-input{left:750px;top:2034px;width:184px;height:38px;background:#252a3b;font-size:10.5px;color:#676c7d;padding:12px 10px}
.news-btn{left:949px;top:2034px;width:80px;height:38px;background:var(--blue);color:var(--white);font-size:16px;line-height:38px;text-align:center}
.footer-rule{left:171px;top:2110px;width:858px;height:1px;background:#2c3142}
.copyright{left:171px;top:2136px;font-size:11px;color:var(--footer-text)}
.social-bottom{left:893px;top:2133px;display:flex;gap:5px}
.social-bottom span{width:23px;height:23px;border-radius:50%;border:1px solid #596074}
</style>
</head>
<body>

<!-- header -->
<div class="abs brand"><div class="brand-square"></div><div class="brand-name">Colbury</div></div>
<div class="abs social-top"><span></span><span></span><span></span><span></span></div>
<div class="abs search">Search</div>
<div class="abs search-btn">
  <svg width="12" height="12" viewBox="0 0 12 12"><circle cx="5" cy="5" r="3.6" fill="none" stroke="#888" stroke-width="1.4"/><line x1="7.6" y1="7.6" x2="11" y2="11" stroke="#888" stroke-width="1.6"/></svg>
</div>

<!-- navigation -->
<nav class="abs nav">
  <a style="left:171px">Home</a><span class="sep" style="left:241px"></span>
  <a style="left:271px">Auctions</a><span class="sep" style="left:358px"></span>
  <a style="left:389px">Real Estate Listings</a><span class="sep" style="left:558px"></span>
  <a style="left:582px">Buyers</a><span class="sep" style="left:660px"></span>
  <a style="left:687px">Sellers</a><span class="sep" style="left:764px"></span>
  <a style="left:790px">About Us</a><span class="sep" style="left:888px"></span>
  <a style="left:912px">Contact Us</a>
</nav>

<!-- slideshow -->
<div class="abs hero" role="img" aria-label="Slideshow photo of a farm with green fields, barns and grain silos under a cloudy sky"></div>
<div class="abs dropdown">
  <a class="first">Our Featured Listings</a>
  <a class="second">Real Estate Listings</a>
</div>
<div class="abs hero-caption">
  <h1>Real Estate Auction</h1>
  <p>Lorem ipsum dolor sit amet, consectetur adipisicing elit, sed do eiusmod tempor incididunt ut labore et dolore magna aliqua.</p>
</div>
<div class="abs hero-arrow" style="left:55px"><svg width="12" height="14" viewBox="0 0 12 14"><polyline points="8,2 3,7 8,12" fill="none" stroke="#fff" stroke-width="2.2"/></svg></div>
<div class="abs hero-arrow" style="left:1105px"><svg width="12" height="14" viewBox="0 0 12 14"><polyline points="4,2 9,7 4,12" fill="none" stroke="#fff" stroke-width="2.2"/></svg></div>

<!-- welcome + video -->
<div class="abs video" role="img" aria-label="Featured video still of a two storey farmhouse on a lawn"></div>
<svg class="abs" style="left:293px;top:723px" width="30" height="34" viewBox="0 0 30 34"><polygon points="4,3 27,17 4,31" fill="rgba(255,255,255,.85)"/></svg>
<div class="abs video-bar">
  <svg width="9" height="10" viewBox="0 0 9 10"><polygon points="0,0 9,5 0,10" fill="#fff"/></svg>
  <span>12:10</span>
  <div class="video-track"><i></i></div>
  <span>08:20</span>
  <svg width="12" height="10" viewBox="0 0 12 10"><polygon points="0,3 3,3 7,0 7,10 3,7 0,7" fill="#fff"/><line x1="9" y1="3" x2="12" y2="7" stroke="#fff"/><line x1="12" y1="3" x2="9" y2="7" stroke="#fff"/></svg>
</div>
<h2 class="abs welcome-title">Welcome To Real Estate Auction</h2>
<p class="abs welcome-text">Lorem ipsum dolor sit amet, consectetur adipisc ng elit. Proin ultricies vestibulum velit, bibendum condimentum metus faucibus sed. Lorem ipsum dolor sit amet, consectetur adipisc ng elit. Proin ultricies vestibulum velit, bibendum condimentum metus faucibus sed. Lorem ipsum dolor sit amet, consectetur adipisc ng elit. Proin ultricies vestibulum velit, bibendum condimentum metus faucibus sed. Lorem ipsum dolor sit amet, consectetur adipisc ng elit. Proin ultricies vestibulum velit, bibendum condimentum</p>
<div class="abs badge" style="left:462px;width:41px"></div>
<div class="abs badge" style="left:517px;width:115px"></div>
<div class="abs badge outline" style="left:646px;width:99px"></div>
<div class="abs badge outline" style="left:760px;width:39px;border-radius:50%"></div>

<!-- featured properties -->
<h3 class="abs section-title" style="top:879px">Featured Properties</h3>
<div class="abs pager" style="left:985px;top:884px">
  <span><svg width="6" height="8" viewBox="0 0 6 8"><polyline points="4.5,1 1.5,4 4.5,7" fill="none" stroke="#777" stroke-width="1.3"/></svg></span>
  <span><svg width="6" height="8" viewBox="0 0 6 8"><polyline points="1.5,1 4.5,4 1.5,7" fill="none" stroke="#777" stroke-width="1.3"/></svg></span>
</div>

<div class="abs card" style="left:171px;top:930px;height:302px">
  <div class="card-img" style="height:174px;background:linear-gradient(180deg,#9fb4c8,#8a6a4c 55%,#4f7d35)" role="img" aria-label="Photo of an old stone and brick cottage with garden"></div>
  <div class="card-body"><div class="card-title">Adipisicing Elit Seddo</div>
  <div class="card-meta"><span class="stars">★★★<b>★★</b></span><span>10,000 Sq. M</span></div>
  <p class="card-text">Lorem ipsum dolor sit amet, eiusmod tempor incididunt</p></div>
</div>
<div class="abs card" style="left:389px;top:930px;height:302px">
  <div class="card-img" style="height:174px;background:linear-gradient(180deg,#4f86c8,#b9a888 50%,#4e8a2c)" role="img" aria-label="Photo of a large beige family house with lawn"></div>
  <div class="card-body"><div class="card-title">Adipisicing Elit Seddo</div>
  <div class="card-meta"><span class="stars">★★★<b>★★</b></span><span>10,000 Sq. M</span></div>
  <p class="card-text">Lorem ipsum dolor sit amet, eiusmod tempor incididunt</p></div>
</div>
<div class="abs card" style="left:607px;top:930px;height:302px">
  <div class="card-img" style="height:174px;background:linear-gradient(180deg,#3f7fd0,#c2c0b4 50%,#5b8a34)" role="img" aria-label="Photo of a white suburban house with front garden"></div>
  <div class="card-body"><div class="card-title">Adipisicing Elit Seddo</div>
  <div class="card-meta"><span class="stars">★★★<b>★★</b></span><span>10,000 Sq. M</span></div>
  <p class="card-text">Lorem ipsum dolor sit amet, eiusmod tempor incididunt</p></div>
</div>
<div class="abs card" style="left:825px;top:930px;height:302px">
  <div class="card-img" style="height:174px;background:linear-gradient(180deg,#b8cbdb,#d8cdb8 45%,#4f7f35)" role="img" aria-label="Photo of a cream house with porch among trees"></div>
  <div class="card-body"><div class="card-title">Adipisicing Elit Seddo</div>
  <div class="card-meta"><span class="stars">★★★<b>★★</b></span><span>10,000 Sq. M</span></div>
  <p class="card-text">Lorem ipsum dolor sit amet, eiusmod tempor incididunt</p></div>
</div>

<!-- featured auctions -->
<h3 class="abs section-title" style="top:1251px">Featured Auctions</h3>
<div class="abs pager" style="left:985px;top:1256px">
  <span><svg width="6" height="8" viewBox="0 0 6 8"><polyline points="4.5,1 1.5,4 4.5,7" fill="none" stroke="#777" stroke-width="1.3"/></svg></span>
  <span><svg width="6" height="8" viewBox="0 0 6 8"><polyline points="1.5,1 4.5,4 1.5,7" fill="none" stroke="#777" stroke-width="1.3"/></svg></span>
</div>

<div class="abs card" style="left:171px;top:1302px;height:303px">
  <div class="card-img" style="height:133px;background:linear-gradient(180deg,#3f78c6,#d4d8dc 45%,#49822c)" role="img" aria-label="Photo of a white house with dark roof and lawn"></div>
  <div class="card-body"><div class="card-title">Excepteur sint occaecat</div>
  <div class="card-meta"><span class="stars">★★★<b>★★</b></span></div>
  <p class="card-text">Lorem ipsum dolor sit amet, eiusmod tempor incididunt</p></div>
</div>
<div class="abs card" style="left:389px;top:1302px;height:303px">
  <div class="card-img" style="height:133px;background:linear-gradient(180deg,#7fa9d8,#a08563 50%,#5c7a3a)" role="img" aria-label="Photo of a brown stone house with gabled roof"></div>
  <div class="card-body"><div class="card-title">Excepteur sint occaecat</div>
  <div class="card-meta"><span class="stars">★★★<b>★★</b></span></div>
  <p class="card-text">Lorem ipsum dolor sit amet, eiusmod tempor incididunt</p></div>
</div>
<div class="abs card" style="left:607px;top:1302px;height:303px">
  <div class="card-img" style="height:133px;background:linear-gradient(180deg,#3d6fc2,#d3bfa0 45%,#4c4c52 80%,#4f8a2e)" role="img" aria-label="Photo of a tan house with garage and driveway"></div>
  <div class="card-body"><div class="card-title">Excepteur sint occaecat</div>
  <div class="card-meta"><span class="stars">★★★<b>★★</b></span></div>
  <p class="card-text">Lorem ipsum dolor sit amet, eiusmod tempor incididunt</p></div>
</div>
<div class="abs card" style="left:825px;top:1302px;height:303px">
  <div class="card-img" style="height:133px;background:linear-gradient(180deg,#a9c6e4,#e2e4e4 45%,#4f8d2c)" role="img" aria-label="Photo of a farmhouse behind a white fence"></div>
  <div class="card-body"><div class="card-title">Excepteur sint occaecat</div>
  <div class="card-meta"><span class="stars">★★★<b>★★</b></span></div>
  <p class="card-text">Lorem ipsum dolor sit amet, eiusmod tempor incididunt</p></div>
</div>

<!-- news & events -->
<h3 class="abs section-title" style="top:1626px">News &amp; Events</h3>
<div class="abs rule"></div>

<div class="abs news-img" style="left:174px;top:1691px;background:linear-gradient(180deg,#c7d6e4,#a79f94 45%,#5a8a3a)" role="img" aria-label="Photo of a family in front of their new home"></div>
<div class="abs news-body" style="left:385px;top:1688px">
  <div class="news-title">Lorem ipsum dolor sit amet</div>
  <div class="news-date">August 10, 2014</div>
  <p class="news-text">Lorem ipsum dolor sit amet, consectetuer adipiscing elit, sed diam nonummy nibh euismod tincidunt ut laoreet dolore Lorem ipsum dolor sit amet, consectetuer</p>
  <div class="news-link">Click HERE +</div>
</div>

<div class="abs news-img" style="left:615px;top:1691px;background:linear-gradient(180deg,#c4ced8,#7e8883 45%,#4d7c33)" role="img" aria-label="Photo of a grey two storey house with porch"></div>
<div class="abs news-body" style="left:825px;top:1688px">
  <div class="news-title">Lorem ipsum dolor sit amet</div>
  <div class="news-date">August 10, 2014</div>
  <p class="news-text">Lorem ipsum dolor sit amet, consectetuer adipiscing elit, sed diam nonummy nibh euismod tincidunt ut laoreet dolore Lorem ipsum dolor sit amet, consectetuer</p>
  <div class="news-link">Click HERE +</div>
</div>

<!-- footer -->
<footer class="abs footer"></footer>
<div class="abs footer-brand"><div class="sq"></div><span>Colbury</span></div>
<p class="abs footer-about">Lorem ipsum dolor sit amet, consectetur adipisicing elit, sed do eiusmod tempor incididunt ut labore et dolore magna aliqua. Ut enim ad minim veniam, quis nostrud exercitation ullamco laboris nisi ut aliquip</p>

<div class="abs footer-head" style="left:488px">ADDRESS</div>
<div class="abs addr-row" style="top:1980px">
  <svg width="13" height="17" viewBox="0 0 13 17"><path d="M6.5 1a5 5 0 0 1 5 5c0 4-5 10-5 10s-5-6-5-10a5 5 0 0 1 5-5z" fill="none" stroke="#8a8fa0" stroke-width="1.5"/><circle cx="6.5" cy="6" r="1.8" fill="#8a8fa0"/></svg>
  <span>42 Marlow Ridge Lane<br>Hollis Park</span>
</div>
<div class="abs addr-row" style="top:2024px">
  <svg width="14" height="12" viewBox="0 0 14 12"><path d="M1 4c0-2 2-3 6-3s6 1 6 3v1h-3V3.5H4V5H1z M3 6h8l1 5H2z" fill="#8a8fa0"/></svg>
  <span>Call us: +1 (555) 014-2290</span>
</div>
<div class="abs addr-row" style="top:2056px">
  <svg width="14" height="11" viewBox="0 0 14 11"><rect x="1" y="1" width="12" height="9" fill="none" stroke="#8a8fa0" stroke-width="1.3"/><polyline points="1,1 7,6 13,1" fill="none" stroke="#8a8fa0" stroke-width="1.3"/></svg>
  <span>info@colbury.com</span>
</div>

<div class="abs footer-head" style="left:747px">NEWSLETTER</div>
<p class="abs newsletter-text">Excepteur sint occaecat cupidatat non proident, sunt in culpa qui officia deserunt mollit anim id est laborum.</p>
<div class="abs news-input">Enter your email address</div>
<div class="abs news-btn">Sign Up</div>

<div class="abs footer-rule"></div>
<div class="abs copyright">© 2014 Colbury - All Rights Reserved</div>
<div class="abs social-bottom"><span></span><span></span><span></span><span></span></div>

</body>
</html>
```